Four Quiet Steps Toward a Stronger Offer on THE Property - VARN Real Estate

I have written an E-Book that is called "Four Quiet Steps Toward a Stronger Offer on The Property." The E-Book will be available as a FREE download from my VARN Real Estate landing page, and also from a Chatterbox campaign that will be commencing in early September.

The E-Book content is in the WORD document below - I now need for it to be made to look more professional and suitable for publishing and placed on my landing page for download. Please review and send me some proposals for this e-book to be a bit more eye catching and appealing than just a WORD doc.

My VARN Real Estate landing page is still under development and you can see the what is close to the final proposal here:

http://www.plum-orbit.com.au/varn/

The cover of the E-Book is at the bottom of the page. Please review and give the internals the sale look and feel.

Target Market(s)

Home and Property Owners in the middle ring Eastern Suburbs of Melbourne - approximately 15 - 30 km's from the central business district. The area is a very family oriented area and features mostly houses that are 3 or 4 bedroom - with some larger properties that are five or more bedrooms. The area is quite an expensive suburban community and house prices range between the low of $1,000,000 to a high of more than $2,500,000. The predominant cultural group that buys in this area are Chinese and Chinese Australian buyers. The predominant group who are selling are usually Australians of a white anglo-saxon background. Other groups are of Asian sub continent background (Indian / Sri Lankan/ Pakistan). All are families that are attracted to the area because of the great schools, good shopping, leisure facilities (parks, pools, courts etc), and excellent public and road transport infrastructure. Read the content of my e-book - it tells you every thing you need to know :)

Industry/Entity Type

Real Estate

Colors

Designer to choose colors to be used in the design.

Requirements
Must have
• Once completed the layout should not be too busy - it should be easy to read. I guess then the statement "less is more" is applicable.
• I will probably print a number of copies of this book for distribution as well - so please consider print attributes in the design.
• IMPORTANT: as for any e-book offering specialist advice, the MAIN reason for the book is for the generation of sales leads and to establish the author as a subject matter expert on the topic. Please consider this in your design elements. BUT - the book should also not come across as 1 big advertisement either. Subtle but impactful are well chosen words to describe how it should present.
Nice to have
• VARN Real Estate branding on every page - to re-inforce the message.
Should not have
• No need for animations or illustrations/

```html
<!DOCTYPE html>
<html lang="en">
<head>
<meta charset="utf-8">
<title>VARN Real Estate – E-Book Spreads</title>
<link href="https://fonts.googleapis.com/css2?family=Montserrat:wght@600;700&family=Oswald:wght@500;600&family=Open+Sans:ital,wght@0,400;0,700;1,400;1,700&display=swap" rel="stylesheet">
<style>
:root{
  --ink:#262829;
  --charcoal:#2e3032;
  --mint:#3fd0a4;
  --mint-dark:#27b588;
  --text:#4a4c4e;
  --paper:#ffffff;
  --canvas:#ffffff;
}
*{box-sizing:border-box;margin:0;padding:0}
html,body{width:1200px;height:1200px;overflow:hidden;background:var(--canvas)}
.sheet{position:relative;width:1200px;height:1200px}
.page{position:absolute;width:276px;height:389px;background:var(--paper);overflow:hidden;box-shadow:0 0 0 .5px #ddd}
.col1{left:29px}.col2{left:319px}.col3{left:609px}.col4{left:899px}
.row1{top:7px}.row2{top:409px}.row3{top:804px}
.page-head{position:absolute;top:0;left:0;width:276px;height:60px}
.brand{position:absolute;top:15px;left:0;width:100%;text-align:center;color:var(--ink)}
.brand-name{font:700 25px/1 'Montserrat',sans-serif;letter-spacing:2px}
.brand-sub{font:600 4px/1 'Montserrat',sans-serif;letter-spacing:3px;margin-top:2px}
.page-foot{position:absolute;bottom:0;left:0;width:276px;height:14px}
.content{position:absolute;top:62px;left:18px;right:18px;font:3.9px/1.48 'Open Sans',sans-serif;color:var(--text);text-align:justify}
.content p{margin-bottom:2.6px}
.title{font:600 8px/1.2 'Oswald',sans-serif;color:var(--ink);letter-spacing:.3px;margin-bottom:4px;text-transform:uppercase;text-align:left}
.title em{font-style:normal;color:var(--mint)}
.sub{display:flex;align-items:center;gap:3px;font:700 5px/1 'Open Sans',sans-serif;color:var(--ink);margin:4px 0 3px;text-align:left}
.sub em{color:var(--mint);text-decoration:underline}
.dot{width:8px;height:8px;border-radius:50%;background:var(--mint);flex:none}
.ticks{list-style:none;margin:2px 0 3px}
.ticks li{position:relative;padding-left:9px;margin-bottom:2px}
.ticks li::before{content:"";position:absolute;left:0;top:.4px;width:4.2px;height:4.2px;border:.6px solid var(--mint);border-radius:50%}
.link{color:var(--mint-dark);font-style:italic}
.photo{position:absolute;left:0;width:276px}
.cover{background:var(--charcoal)}
.cover-brand{position:absolute;top:14px;left:18px;color:#fff}
.cover-brand .brand-name{font-size:22px}
.cover-strip{position:absolute;top:258px;left:0;width:100%;height:20px;background:var(--charcoal);color:#fff;font:500 9px/20px 'Oswald',sans-serif;padding-left:22px;letter-spacing:.3px}
.cover-strip em{font-style:normal;color:var(--mint)}
.cover-body{position:absolute;top:278px;left:0;width:100%;height:111px;background:#fff;padding:9px 22px 0}
.cover-title{font:600 16px/1.05 'Oswald',sans-serif;color:var(--ink)}
.cover-tag{font:500 10.5px/1.1 'Oswald',sans-serif;color:var(--mint);letter-spacing:.2px;margin-bottom:5px}
.cover-body p{font:3.6px/1.45 'Open Sans',sans-serif;color:var(--text);margin-bottom:2px;text-align:justify}
.chart-label{font:600 7px 'Oswald',sans-serif;fill:#fff}
.pyr-label{font:700 6px 'Open Sans',sans-serif;fill:#fff}
.cta{font:600 19px/1.05 'Oswald',sans-serif;color:var(--ink);text-align:left}
.cta em{font-style:normal;color:var(--mint)}
.two-col{display:flex;gap:10px}
.two-col ul{flex:1}
.lead{color:var(--mint-dark);text-align:center;text-transform:uppercase}
</style>
</head>
<body>
<div class="sheet">

<svg width="0" height="0" style="position:absolute" aria-hidden="true">
  <defs>
    <symbol id="head" viewBox="0 0 276 60">
      <path d="M0 0H276V30L138 6L0 30Z" fill="#2e3032"/>
      <polyline points="0,33 138,9 276,33" fill="none" stroke="#3fd0a4" stroke-width="1.4"/>
    </symbol>
    <symbol id="foot" viewBox="0 0 276 14">
      <rect y="4" width="276" height="10" fill="#3fd0a4"/>
      <path d="M40 14L150 3L276 14Z" fill="#2e3032"/>
    </symbol>
  </defs>
</svg>

<!-- Page 1 : cover -->
<section class="page cover col1 row1">
  <svg class="photo" style="top:0;height:258px" viewBox="0 0 276 258" role="img" aria-label="Photo of a smiling family with two young children sitting together in a bright living room">
    <defs><linearGradient id="g1" x1="0" y1="0" x2="0" y2="1"><stop offset="0" stop-color="#e9e4dc"/><stop offset="1" stop-color="#b9a48c"/></linearGradient></defs>
    <rect width="276" height="258" fill="#2e3032"/>
    <polygon points="8,258 8,100 150,14 268,100 268,258" fill="url(#g1)"/>
    <polyline points="4,102 150,10 272,102" fill="none" stroke="#fff" stroke-width="2"/>
  </svg>
  <div class="cover-brand"><div class="brand-name">VARN</div><div class="brand-sub">REAL ESTATE</div></div>
  <div class="cover-strip">CITY OF MONASH &amp; <em>CITY OF WHITEHORSE</em></div>
  <div class="cover-body">
    <div class="cover-title">FOUR QUIET STEPS TOWARD</div>
    <div class="cover-tag">A STRONGER OFFER ON THE PROPERTY</div>
    <p>So after much consideration you have made the decision to sell your property. For some of you the home may have held many long and happy memories. For others it was a property purchased purely as an investment vehicle to build wealth. Unfortunately for some others it may be necessary to sell due to life challenges, whether they be financial issues, a marriage breakdown or the passing away of a family member. Whatever the reason and your motivation for selling, once the decision to sell is made, the most important end result is to get the very best price possible in the market place.</p>
    <p>In this free e-book you will find four quiet steps toward a stronger offer on the property. It includes some useful tips to help you prepare your property to be put on the market for sale, and what to do next to extract top dollar for the sale of your home.</p>
  </div>
  <svg class="page-foot" aria-hidden="true"><use href="#foot"/></svg>
</section>

<!-- Page 2 -->
<section class="page col2 row1">
  <svg class="page-head" aria-hidden="true"><use href="#head"/></svg>
  <div class="brand"><div class="brand-name">VARN</div><div class="brand-sub">REAL ESTATE</div></div>
  <div class="content">
    <div class="title" style="text-transform:none;font-size:7px"><em>By the way....CONGRATULATIONS</em> on your choice of location:</div>
    <p>The desirable and leafy cities in the east are exceptionally popular residential localities, and it is little wonder when you consider all that they offer to the modern family. The standout features of these two great municipalities include:</p>
    <ul class="ticks">
      <li><span class="link">Superb education options</span> – some of the city's leading government and private primary and secondary schools are located within the boundaries of both cities. There are also excellent tertiary education choices nearby, and a great choice of childcare and kindergarten options for local families.</li>
      <li><span class="link">Outstanding shopping</span> exists and includes large shopping centres, village shopping strips and a wide range of smaller local and specialty stores.</li>
      <li><span class="link">Beautiful parks, trails and outdoor leisure facilities</span> including reserves, lakes, golf courses, sporting clubs and walking and cycling trails.</li>
      <li>A large number of <span class="link">public transport choices</span> for commuters and students spread right across the region including trains, trams and buses.</li>
      <li><span class="link">Excellent freeway and road infrastructure</span> that is continuously evolving and linking the eastern suburbs with all parts of the city.</li>
    </ul>
    <p>Education, shopping and transport infrastructure form the backbone of any desirable community and the attraction of families, investors and developers to these popular and well established residential areas ensures that the foundation for interest in your property is already in place. So in order for your home to sell well and achieve the best possible price, here are the <span class="link">Four Quiet Steps Toward a Stronger Offer on The Property</span> to help you on your journey.</p>
  </div>
  <svg class="photo" style="top:238px;height:137px" viewBox="0 0 276 137" role="img" aria-label="Photo of a family lying together on a living room floor">
    <defs><linearGradient id="g2" x1="0" y1="0" x2="1" y2="1"><stop offset="0" stop-color="#f1ede6"/><stop offset="1" stop-color="#c9b39b"/></linearGradient></defs>
    <rect width="276" height="137" fill="url(#g2)"/>
  </svg>
  <svg class="page-foot" aria-hidden="true"><use href="#foot"/></svg>
</section>

<!-- Page 3 -->
<section class="page col3 row1">
  <svg class="page-head" aria-hidden="true"><use href="#head"/></svg>
  <div class="brand"><div class="brand-name">VARN</div><div class="brand-sub">REAL ESTATE</div></div>
  <div class="content">
    <div class="title">Property <em>Presentation:</em></div>
    <p>Like any product, the newer, the cleaner, the shinier and the better presented a property is for sale, the more interest it will attract from prospective buyers.</p>
    <p>The more buyer interest that a property attracts, the more competition around the purchase price that will be created.</p>
    <p>And buyer competition is fantastic if you know how to harness it to achieve the best possible sale price. But where is it that you should begin and how?</p>
    <p>So let us start at the very beginning: property preparation and presentation for sale.</p>
    <p>It is important to state that very few people actually live in the manner that a house is presented for sale. In most instances what you see at homes that are open for buyer inspection is the end result of a lot of hard work on behalf of the vendor and others.</p>
    <p>So do not be concerned with how ever and whatever your home looks like now; it can be transformed to maximise its appeal to buyers.</p>
    <p class="link">"Vendors will always see all of the great and wonderful aspects of their property in an effort to create value and push up the price; a buyer will always tell you everything that is wrong in an effort to drive down the price."</p>
    <p>The whole process of buying and selling property is very psychological and highly emotional for most people, so it is very important for vendors to place themselves in the shoes of a buyer when running a critical eye across the presentation preparations.</p>
    <p>Your property should be polished, displayed and presented to the highest possible standard. That standard will be different for everyone, factoring in age, ability, financial capacity, the size of family and the number of pets.</p>
    <p>In addition, every property is different, and every property has its own features and personality; what is important is to amplify the positives and minimise the impact of the negatives throughout the home.</p>
    <p>Let us look at some of the basics:</p>
    <div class="sub"><span class="dot"></span><span><em>Curbside</em> Appeal</span></div>
    <p>First impressions count: stand outside at the front of your house on the street and look at your home with a critical eye. Does your home stand out as a welcoming and happy place to arrive at?</p>
    <p>Tidy the gardens, mow the lawns, repair the gutters, paint under the eaves of the roof, clean the windows, repair the cement driveways and do some basic landscaping such as adding mulch to garden beds. There are other varieties you can choose, but make a difference to the exterior look and feel of your property.</p>
    <p>If your property has a fence, then clean it and paint it. Cut back any overgrown trees and bushes, trim and shape the edges of pathways, and clear and remove all rubbish from the front of the house.</p>
    <p>By improving your property's curbside appeal and street presence you will not only allow buyers to have an immediate positive first impression, you are also ensuring that the property is ready to be photographed for the all important exterior facade shot as part of the marketing and advertising.</p>
  </div>
  <svg class="page-foot" aria-hidden="true"><use href="#foot"/></svg>
</section>

<!-- Page 4 -->
<section class="page col4 row1">
  <svg class="page-head" aria-hidden="true"><use href="#head"/></svg>
  <div class="brand"><div class="brand-name">VARN</div><div class="brand-sub">REAL ESTATE</div></div>
  <div class="content">
    <div class="sub" style="margin-top:2px"><span class="dot"></span><span><em>Cleaning &amp;</em> De-Cluttering</span></div>
    <p>If you have been living in your home for any more than a few years, then you might be surprised at the amount of things that you have accumulated. Most people do not genuinely live in the manner that they present a property when they sell. And less is definitely more when it comes to the sale of your home and the reduction of the things in the home.</p>
    <p>Our friends at <span class="link">www.tidyhome-guide.com.au</span> offer the following tips when it comes to de-cluttering:</p>
    <p>Top tips on how to de-clutter your home:</p>
    <ul class="ticks">
      <li>Just start. Do not overthink it; just start getting rid of things!</li>
      <li>Deal with rubbish first. Start by going through each room with a big garbage bag and throwing away anything that is not saleable or suitable for charity.</li>
      <li>De-clutter by category, not by room. It is less overwhelming to de-clutter by category such as clearing out DVDs or linen than to tackle a whole room.</li>
      <li>It is about progress, not perfection. Do not be discouraged; clutter takes time to build up and it will take time to deal with.</li>
      <li>If you do not need it, why not donate it or throw it away?</li>
      <li>Remove all books from bookcases.</li>
      <li>Pack up those knick knacks.</li>
      <li>Clean off everything on kitchen counters.</li>
      <li>Put essential items used daily in a small box that can be stored in a closet when not in use.</li>
      <li>Think of this process as a head start on the packing you will eventually need to do anyway.</li>
    </ul>
    <p>Of equal importance is the organisation and arrangement of the areas that cannot be immediately seen. Cupboards, closets, linen presses and pantries inside the property. Buyers will open and look inside pantries, cupboards and wardrobes, so the more organised they are the better impression a buyer will have of the property.</p>
    <p>If you have a lot of packing boxes and surplus furniture to be removed and put away, and an off-site storage space is not an option, then a garage on the property can be used so long as items are neatly packed and safely stored.</p>
    <div class="sub"><span class="dot"></span><span><em>Maintenance &amp;</em> Painting</span></div>
    <p>Walk through your property and check that all lights are working (replace the globes if they are not working). Identify and fill any cracks in the walls, float and ceilings, apply a coat of paint externally and internally.</p>
    <p>Paint can hide a lot of sins and also provides a new lease on life for homes that have been well lived in. Weatherboard or timber homes in particular freshen up very well externally following a coat of paint. Professional painters can be expensive if they are required to complete the entire house internally and externally. However, the cost is quite likely recovered through the increased price achieved on the sale of your home.</p>
    <p>No matter what anyone, including agents, will tell you, no buyer is interested in looking at peeling paint, and they will soon start questioning as to what else is wrong in the property and start talking the price down. We do not want that to happen to your property.</p>
  </div>
  <svg class="page-foot" aria-hidden="true"><use href="#foot"/></svg>
</section>

<!-- Page 5 -->
<section class="page col1 row2">
  <svg class="page-head" aria-hidden="true"><use href="#head"/></svg>
  <div class="brand"><div class="brand-name">VARN</div><div class="brand-sub">REAL ESTATE</div></div>
  <div class="content">
    <div class="sub" style="margin-top:2px"><span class="dot"></span><span><em>Professional Home</em> Staging / Styling</span></div>
    <p>One of the best investments you can make in the sale of your home is having your home professionally staged by a stylist.</p>
    <p>Stylists are property presentation experts who concentrate on displaying your property in the best possible manner for sale. A stylist can add tens of thousands of dollars to the price of a property, simply by adding their design creativity.</p>
    <p>For properties that have no furniture, staging is very important in order to engage buyers emotionally in the home. Furniture, window dressings, wall hangings and decorations create the soul of any home. I have experienced many a buyer across the years be disappointed at the final inspection prior to settlement, when they realise what they have purchased is just four walls, a ceiling and an empty room, as it was so beautifully styled and presented as a dream lifestyle at the time of sale.</p>
    <div class="sub"><span class="dot"></span><span><em>Renovation versus</em> Cosmetic Improvement</span></div>
    <p>Renovate and make money! This claim is made constantly but is it true? Would you be better off merely doing some basic cosmetic work to improve presentation rather than renovating?</p>
    <p>Renovating with the purpose of the homeowner staying in the property with an improved lifestyle is quite different to renovating for the purpose of making a profit. It is important to be aware that renovation is no guarantee to making a profit.</p>
    <p>Would-be renovators need to be aware that with respect to the value of a property there are two core forces at work.</p>
    <p>Firstly, there is the land on which the building sits. The price of land appreciates according to market demand and the popularity of the locality. On the other hand most buildings depreciate in value, eventually to the point that their very presence actually devalues a site. In other words the site would be worth more without the building that sits on it.</p>
    <p>Whilst renovating a building undoubtedly improves the value of a property, there's the question as to whether the consequential improvement in value will be sufficient for the investment in the renovation to be profitable.</p>
    <p>Though many people would claim that they have renovated and profited, the question arises would they have profited by a greater amount simply by tidying up and perhaps repainting, thus saving the cost of renovation?</p>
    <p>It is a different matter if you are able to renovate to a professional standard yourself; you are saving the substantial cost of labour. But if you have to hire people, then think about it carefully!</p>
    <p>There is some suggestion that the smaller the land area is, in proportion to the overall property value, so the better the proposition of renovation. In other words a renovation project may be a better proposition for giving a return in an old townhouse or home unit rather than a home on a full block.</p>
    <p>One well known cautionary measure is to weigh the cost of any improvements you want to make against the overall values in your neighbourhood. If you over-improve for the neighbourhood, you may not boost your property value sufficiently to recover the costs, let alone turn the cost into additional profit.</p>
    <p>So in summary, a well presented property is very important in capturing buyer interest and selling your home for the best price. How far you go to create the impression of a perfect lifestyle property is your decision, and your agent can provide advice as to what polishing should be done at a minimum to help you achieve the best price.</p>
  </div>
  <svg class="page-foot" aria-hidden="true"><use href="#foot"/></svg>
</section>

<!-- Page 6 -->
<section class="page col2 row2">
  <svg class="page-head" aria-hidden="true"><use href="#head"/></svg>
  <div class="brand"><div class="brand-name">VARN</div><div class="brand-sub">REAL ESTATE</div></div>
  <div class="content">
    <div class="title">Property <em>Presentation:</em></div>
    <p>There are three prices in the sale of residential property:</p>
    <div class="sub"><span class="dot"></span><span><em>The Logical</em> / Probable Price</span></div>
    <p>The logical and probable price for your home is determined by your agent reviewing data of similar types of properties that have sold around the immediate location of your property across the last six months. Key property features that are considered to establish this estimate of price are:</p>
    <ul class="ticks">
      <li>The number of bedrooms, bathrooms, living areas and car spaces.</li>
      <li>The year that the dwelling was constructed.</li>
      <li>The size and location of the land.</li>
      <li>Proximity to schools, shopping, leisure facilities and transport infrastructure.</li>
    </ul>
    <p>An agent will then estimate the probable market value of the property giving consideration to the aforementioned points.</p>
    <div class="sub"><span class="dot"></span><span><em>Seller's Goal</em> on Price</span></div>
    <p>Every property owner has a goal on price that is personal to him or her and aside from market value. In most cases there is a disparity on an owner's price and market value, and this should be discussed with the agent.</p>
    <div class="sub"><span class="dot"></span><span><em>The Agent's Role</em> in Determining Price</span></div>
    <p>The role that an agent plays in determining price is very important.</p>
    <p>No two homes are the same, each home has its own distinct personality and character.</p>
    <p>The agent's role is to efficiently project manage the sales campaign of your property, match its specific features and personality to the right buyer under the right conditions through negotiation expertise.</p>
    <p>Estimating the correct pricing range for your property is critical in helping it to sell well. An accurate pricing range will attract the right buyers and create competition. Buyer competition combined with elite level agent negotiation skills will result in your property selling for the best price.</p>
  </div>
  <svg class="photo" style="top:290px;height:85px" viewBox="0 0 276 85" role="img" aria-label="Photo of a smiling family with two children posing together">
    <defs><linearGradient id="g6" x1="0" y1="0" x2="1" y2="0"><stop offset="0" stop-color="#fff"/><stop offset=".45" stop-color="#ece3d6"/><stop offset="1" stop-color="#c6a98b"/></linearGradient></defs>
    <rect width="276" height="85" fill="url(#g6)"/>
  </svg>
  <svg class="page-foot" aria-hidden="true"><use href="#foot"/></svg>
</section>

<!-- Page 7 -->
<section class="page col3 row2">
  <svg class="page-head" aria-hidden="true"><use href="#head"/></svg>
  <div class="brand"><div class="brand-name">VARN</div><div class="brand-sub">REAL ESTATE</div></div>
  <div class="content">
    <div class="title"><em>Agent</em> Choice:</div>
    <p>The job of an elite sales agent is not to sell your property, most people can do that. The purpose of an elite sales agent is to get their vendor the hidden extra in the marketplace by following a premium price strategy.</p>
    <p>Selecting the right agent to represent you in the sale of your home is critical. They will represent you and follow your instructions, negotiate with buyers on your behalf, and use their experience and expert judgment to direct the sales campaign to maximise the price of your property.</p>
    <p>The entry point to becoming an estate agent is low, with the only educational requirement being a three day course that mostly focuses on the legislative requirements of the job, not on salesmanship and negotiation expertise. On the successful completion of the three unit course, the sales person may work as an agent's representative in an agency and employed under the control of a fully licensed estate agent or officer-in-effective-control of that agency.</p>
    <p>A fully licensed agent has more than twelve months full time industry experience, and has successfully completed a further units of study in order to gain their licence. Completing that amount of study normally takes many months of part time study to complete while the agent is working full time. A fully licensed agent can apply to the licensing authority to be the officer-in-effective-control of an agency, or be an employee of an agency, or even represent himself or herself as a sole trader.</p>
    <p>All estate agents must be registered with the licensing authority; it is worth viewing the register before deciding on your agent, to check that they are registered. Unregistered agents are in breach of the law and risk significant penalties.</p>
    <p>Most estate agents work as part of a franchise brand or a smaller independent boutique office. The principals of these offices pay a franchise fee in exchange for the use of these brands. It is important to understand that while these are well known and established brands across the city, the agency is an individual business run by its own owner.</p>
    <p>It is the expertise that an agent has, and the sales process that an agent follows, that will get your home sold for the best price. Brand alone makes no difference to the outcome. Buyers follow and look for properties they like; they do not look for estate brands and agents. The competitive estate agency playing field has been equalised between national branded agencies and boutique agencies thanks to the rise of the internet.</p>
    <p>All agencies, large and small, have a database of buyers, most agencies employ the same or similar marketing techniques to sell your home. All agencies have access to stylists and maintenance contractors to best present your home. The difference comes from the capability and expertise of the individual agent, their energy, their professionalism, their ability to negotiate, and their expert communication, accessibility and availability with both the property vendor and the buyers.</p>
    <p>Remember: <span class="link">it is the sale process rather than the promise on price that will get your home sold for top dollar.</span> Talk to your agent and have him or her articulate the sale process. Ask him or her if they will be present for the whole campaign, at every open for inspection, and personally speaking with the buyers to negotiate the very best price? You have one chance to sell your property well, so make sure you choose an expert agent to represent you and confidently direct the selling process.</p>
  </div>
  <svg class="page-foot" aria-hidden="true"><use href="#foot"/></svg>
</section>

<!-- Page 8 -->
<section class="page col4 row2">
  <svg class="page-head" aria-hidden="true"><use href="#head"/></svg>
  <div class="brand"><div class="brand-name">VARN</div><div class="brand-sub">REAL ESTATE</div></div>
  <div class="content">
    <div class="title">Marketing <em>&amp;</em> Advertising</div>
    <p>Next to price, property marketing and advertising is the cause of the greatest amount of vendor stress. Marketing and advertising of residential property is expensive. It feels especially expensive when you are nervously waiting for the outcome of a sales campaign that will justify the cost.</p>
    <p>But do not worry. The right marketing campaign is of significant importance in order for the right buyer to find and actively bid on your property. It is important to understand why you are spending money to sell, and to make sure the spend is invested wisely in each buyer channel.</p>
    <p>The same formula is applied in real estate: marketing and advertising cost can simply be measured by the property owner's return on investment when the property sells at an above market price. There are plenty of agencies that will offer free marketing, usually a third or fourth tier internet only proposal that produces little exposure for the property and attracts a low number of buyers. These agencies charge a hefty sales commission if and when the home eventually sells.</p>
    <p class="link">An elite agent will develop a premium price strategy for your home as follows:</p>
    <ul class="ticks">
      <li>Create an exceptional marketing program that gets buyers to the front door of the home. The foundation of exceptional marketing is beautiful photography, professional and descriptive copywriting, and accurate and clearly drawn floor plans.</li>
      <li>With buyers at the front door of the home, the elite agent will obtain their personal and contact details and then get them inside to experience and connect with the property features.</li>
      <li>The elite agent will then qualify and create competition amongst emotionally engaged buyers using high level negotiation skills.</li>
      <li>And finally, the elite agent will conclude the sale having achieved a price from a winning buyer that defies logic; a price that is purely based on emotion.</li>
    </ul>
    <p>The general guideline for marketing is that a vendor should commit one percent of the logical sale price of the property toward the marketing and advertising budget, with a good agent providing advice on how to spend it.</p>
  </div>
  <svg class="photo" style="top:282px;height:93px" viewBox="0 0 276 93" role="img" aria-label="Photo of a family relaxing together on a sofa in a bright room">
    <defs><linearGradient id="g8" x1="0" y1="0" x2="1" y2="1"><stop offset="0" stop-color="#eef1f2"/><stop offset="1" stop-color="#9fa6ad"/></linearGradient></defs>
    <rect width="276" height="93" fill="url(#g8)"/>
  </svg>
  <svg class="page-foot" aria-hidden="true"><use href="#foot"/></svg>
</section>

<!-- Page 9 -->
<section class="page col1 row3">
  <svg class="page-head" aria-hidden="true"><use href="#head"/></svg>
  <div class="brand"><div class="brand-name">VARN</div><div class="brand-sub">REAL ESTATE</div></div>
  <div class="content">
    <p class="lead" style="margin-top:4px">There are four buyer categories as follows:</p>
    <svg width="240" height="150" viewBox="0 0 240 150" role="img" aria-label="Chart of four buyer categories: local, out of area, passive, active" style="display:block;margin:6px auto 8px">
      <path d="M120 75V10A65 65 0 0 0 55 75Z" fill="#4b4e51"/>
      <path d="M120 75V10A65 65 0 0 1 185 75Z" fill="#4b4e51"/>
      <path d="M120 75H55A65 65 0 0 0 120 140Z" fill="#5c5f62"/>
      <path d="M120 75H185A65 65 0 0 1 120 140Z" fill="#5c5f62"/>
      <line x1="120" y1="10" x2="120" y2="140" stroke="#fff" stroke-width="1.5"/>
      <line x1="55" y1="75" x2="185" y2="75" stroke="#fff" stroke-width="1.5"/>
      <text class="chart-label" x="90" y="58" text-anchor="middle">LOCAL</text>
      <text class="chart-label" x="150" y="52" text-anchor="middle">OUT OF</text>
      <text class="chart-label" x="150" y="61" text-anchor="middle">AREA</text>
      <text class="chart-label" x="90" y="100" text-anchor="middle">PASSIVE</text>
      <text class="chart-label" x="150" y="100" text-anchor="middle">ACTIVE</text>
    </svg>
    <p>A premium price marketing strategy will capture each buyer segment so that one hundred percent of the four possible buyer groups have the opportunity to be introduced to the property.</p>
    <p>Normally this involves a combination of internet advertising on the biggest property portals (active buyers), combined with some form of print advertising (passive buyers).</p>
    <p>This ensures that the advertising net is thrown far enough that it captures and brings every type of buyer to the property. This is also where the largest marketing cost is, the actual advertising of the property on the online portals and in print media.</p>
    <p>Other smaller cost, but equally important, marketing vehicles are auction and for sale boards outside the house featuring photos showing a glimpse of the inside of the property; property brochures for buyers to take away with them at open for inspections so as to remind them of all the attributes and personality that the house had to offer.</p>
    <p class="link">Important: the sale of your property is not in isolation; it is in competition with other similar properties that are selling at the same time.</p>
    <p>I have personally seen vendors lose tens of thousands of dollars on price because they insisted on saving a few thousand dollars on marketing at the start of a campaign.</p>
    <p>Marketing and advertising for the sale of your property should be seen as an investment in price success, and like any investment, by attracting the right buyers to your property you should expect to see much more in profit return than your initial investment in marketing.</p>
  </div>
  <svg class="page-foot" aria-hidden="true"><use href="#foot"/></svg>
</section>

<!-- Page 10 -->
<section class="page col2 row3">
  <svg class="page-head" aria-hidden="true"><use href="#head"/></svg>
  <div class="brand"><div class="brand-name">VARN</div><div class="brand-sub">REAL ESTATE</div></div>
  <div class="content">
    <div class="title"><em>Methods</em> of Sale</div>
    <p>Private sale, off market sale, auction, expressions of interest, sale by set date, sale by tender: the list of different methods of sale goes on and on.</p>
    <p>Many a vendor has been called upon, either by telephone or by a knock on the front door, and told by an excited real estate sales agent that he and his agency have hot buyers looking to make an offer on your property right now.</p>
    <p class="link">"Please, please Mr Owner, if you are interested in selling just sign this exclusive sale authority and we will bring them through."</p>
    <p>Of course many of the hot buyers will then simply evaporate. "I am sorry Mr Owner, unfortunately they purchased somewhere else." "But never fear, we can now take your property to the public market and sell by private sale or auction... your choice."</p>
    <p class="link" style="font-style:normal">Beware pushy agent sales tactics. The first price is never the best price.</p>
    <svg width="150" height="88" viewBox="0 0 150 92" role="img" aria-label="Pyramid of buyer types: emotional, probable, bargain hunter" style="display:block;margin:4px auto 5px">
      <polygon points="75,2 100,32 50,32" fill="#3b3d40"/>
      <polygon points="48,35 102,35 122,60 28,60" fill="#3b3d40"/>
      <polygon points="26,63 124,63 146,90 4,90" fill="#3b3d40"/>
      <text class="pyr-label" x="75" y="27" text-anchor="middle" style="font-size:4.5px">Emotional</text>
      <text class="pyr-label" x="75" y="51" text-anchor="middle">Probable</text>
      <text class="pyr-label" x="75" y="80" text-anchor="middle" style="font-size:7px">Bargain Hunter</text>
    </svg>
    <p>There are many different ways to sell your property. However, the title of this e-book is <span class="link">Four Quiet Steps Toward a Stronger Offer on The Property.</span></p>
    <p>So Mr and Mrs Property Owner, if I can show you a method of selling your property to the widest buyer audience, with a set time frame within which buyers must take action, and a process that creates buyer competition to maximise price, and finally have a contract of sale signed on the day, would you be open to hearing it? Of course you would. Let me introduce you to <span class="link">sale by auction!</span></p>
    <p>The most widely utilised sales vehicle for the effective sale of property across the eastern suburbs is sale by auction. In fact, an auction is still the most common method of residential real estate property sales across the city on most weekends.</p>
    <p>The majority of these properties sell, with recent clearance rates being well above seventy percent. That means that more than seven of every ten properties auctioned sell each weekend, which is testimony to the fact that sale by auction works!</p>
  </div>
  <svg class="page-foot" aria-hidden="true"><use href="#foot"/></svg>
</section>

<!-- Page 11 -->
<section class="page col3 row3">
  <svg class="page-head" aria-hidden="true"><use href="#head"/></svg>
  <div class="brand"><div class="brand-name">VARN</div><div class="brand-sub">REAL ESTATE</div></div>
  <div class="content">
    <p class="link" style="font-style:normal;font-weight:700;margin-top:2px">The benefits of utilising an auction campaign to sell your property is:</p>
    <ul class="ticks">
      <li>An auction sales campaign is a short sharp campaign that has a defined start and close date (auction day) by which time buyers need to have made a decision as to whether they are participating or otherwise. There is no lingering over the decision-making.</li>
      <li>Buyers are bidding for property in a competitive environment against other buyers. Buyers do not like what competition does to the price of a property but they do like the social proof of auctions that shows that other buyers are also interested in the property they are bidding on. This creates emotion and drives bidders at auction to bid well above the logical price.</li>
      <li>The contract of sale is signed and exchanged by buyer and vendor at auction unconditionally. There is no cooling off period as there is with a private sale, there can be no subject to finance clauses, no subject to building inspections, no subject to pest inspections. Anything at auction, the property is sold if bought at auction, a deposit is taken, and the buyer rescinds on the contract and loses that deposit.</li>
      <li>An auction offers the vendor reserve price protection, which means that a property will not sell unless a pre-agreed price is reached. And there is no ceiling once the reserve has been reached; bidding may well continue well above the reserve price, especially if there is strong competition.</li>
    </ul>
    <p>Preparing for and sitting through an auction campaign is a challenge, especially on the nerves of any vendor faced with the uncertainty of the final outcome.</p>
    <p>But, an experienced sale agent will direct the campaign, keep you informed as to the progress and the number of buyers who are interested in your property, and communicate with and prepare the buyers in advance of the auction to ensure the best outcome.</p>
    <p>And yes, there is risk that bidding at auction will not be sufficient to reach a vendor's reserve price on the day. But that should come as no surprise to an agent who has run, directed and controlled an effective sales campaign, and a plan should be in place to deal with it and sell the house after.</p>
    <p>And if the property passes in at auction, then it simply transfers over to a private sale whereby individual buyers are negotiated with on price individually in an effort to meet the vendor's reserve.</p>
    <p>On the other hand, the reward is immense: bidding at auction is vigorous, the reserve is quickly reached and exceeded, the property is declared on the market and buyers are now bidding to buy with energy and emotion. This is the place where the hidden extra on price is found and the winning bidder is declared the new owner of the property at a price that well exceeds the reserve.</p>
    <p>The result and the outcome of a successful and professionally run auction sales campaign will definitely uncover the hidden extra on price in the marketplace, maximising the sale price of the property, and has the ability to change people's lives financially.</p>
    <p>An agent that is chosen to represent a vendor in the sale of their home holds an enormous amount of responsibility. Make sure you ask the agent to explain their auction process. Ask him or her who is present on auction day and how the reserve is set. Check the agent's auction processes by going to watch some of his or her auctions prior to placing your property in their hands. Did they remain in control of the auction and the buyers? Did they get the sold sticker up on the board?</p>
    <p>Do not be afraid to ask questions and challenge an agent on his or her processes. An elite agent will be knowledgeable, intelligent and present as a property sales expert. They will simply be delighted to share the information with you.</p>
  </div>
  <svg class="page-foot" aria-hidden="true"><use href="#foot"/></svg>
</section>

<!-- Page 12 -->
<section class="page col4 row3">
  <svg class="page-head" aria-hidden="true"><use href="#head"/></svg>
  <div class="brand"><div class="brand-name">VARN</div><div class="brand-sub">REAL ESTATE</div></div>
  <div class="content">
    <div class="title"><em>Conclusion</em></div>
    <p>So when it comes to selling your property anywhere across the eastern suburbs, it all starts with a solid and proven strategy. Follow the <span class="link">Four Quiet Steps Toward a Stronger Offer on The Property:</span></p>
    <div class="two-col">
      <ul class="ticks"><li>Property presentation</li><li>Pricing</li><li>Agent choice</li></ul>
      <ul class="ticks"><li>Marketing and advertising</li><li>Methods of sale</li></ul>
    </div>
    <p>I have used this successful strategy time and time again to help my clients achieve top dollar in the sale of their home. At VARN Real Estate we are property sales experts.</p>
    <p>Most people buy and sell one or two properties in a lifetime. At VARN Real Estate we transact property sales every week and we know what works in getting you the best possible price for your home.</p>
    <p>Get us in for a chat and an assessment of your requirements in the sale of your property. I know you will not be disappointed that you did.</p>
    <div class="cta" style="margin-top:10px">GET IN TOUCH WITH<br><em>VARN REAL ESTATE NOW</em></div>
  </div>
  <svg class="photo" style="top:268px;height:107px" viewBox="0 0 276 107" role="img" aria-label="Photo of the agent in a suit standing in front of a brick family home">
    <defs>
      <linearGradient id="g12" x1="0" y1="0" x2="0" y2="1"><stop offset="0" stop-color="#dfe7ec"/><stop offset="1" stop-color="#7f8c6e"/></linearGradient>
      <linearGradient id="g12b" x1="0" y1="0" x2="0" y2="1"><stop offset="0" stop-color="#c9b6a4"/><stop offset="1" stop-color="#2c2f35"/></linearGradient>
    </defs>
    <polygon points="0,40 90,0 180,40 180,107 0,107" fill="url(#g12)"/>
    <rect x="170" y="0" width="106" height="107" fill="url(#g12b)"/>
  </svg>
  <svg class="page-foot" aria-hidden="true"><use href="#foot"/></svg>
</section>

</div>
</body>
</html>
```